Design Card that Captures Life's Moments

Thinking black and white design with maybe some accent colors. Open to others too. Looking for bold and modern to accompany new logo design. For the side without my info, would have tagline of "Capturing Life's Moments" with either logo or website petravossimaging.com. I want the tagline to dominate and be the main focus of that side.

Target Market(s)

Something that can appeal to people who might be interested in family/kids, business, sports, commercial, or birth/newborn photography.

Industry/Entity Type

Professional Photography

Contact Information for Business Card

Font styles to use
Sans Serif
Script
Other font styles liked:
• Go with Logo, but the tagline could be script that popped.

Requirements
Must have
• See details above! Wow factor! Make someone pick my card up and take it home or at least to look at it further.
• Tagline: Capturing Life's Moments (Main text on side without name)
• INFO:
• Petra Voss-Hale - Photographer
• 555-318-0462 - Cell and for SMS
• www.petravossimaging.com - Website (maybe on side with tagline?)
• petra@petrastudioframes.com - Email
Nice to have
• JUST AN IDEA... I would like to see Capturing Life's Moment really take over most of one side of the card. Think greeting card. Where you can't miss it. It is in your face, but nice and elegant. Maybe cursive, but could work with other font. Instead of logo on tagline side, just have petravossimaging.com in smaller text along one of the edges.
Should not have
• Too simple I could of created it, like with only my logo and some typed text.

```html
<!DOCTYPE html>
<html lang="en">
<head>
<meta charset="utf-8">
<title>Petra Voss-Hale – Business Card</title>
<link rel="stylesheet" href="https://fonts.googleapis.com/css2?family=Didact+Gothic&family=Montserrat:wght@400;700;800&display=swap">
<style>
  :root {
    --backdrop: #d9d6d2;
    --card-black: #151515;
    --card-charcoal: #1e1e1e;
    --band-white: #f4f4f4;
    --ink-white: #ffffff;
    --ink-grey: #b9b9b9;
    --ink-dark: #1a1a1a;
    --photo-teal: #2a6f73;
    --photo-violet: #4e3d66;
  }
  * { margin: 0; padding: 0; box-sizing: border-box; }
  html, body {
    width: 1200px; height: 873px; overflow: hidden;
    background: var(--backdrop);
  }
  .canvas {
    position: relative; width: 1200px; height: 873px;
    display: flex; align-items: center; justify-content: center; gap: 44px;
  }
  .card {
    position: relative; width: 540px; height: 309px; overflow: hidden;
    box-shadow: 0 10px 28px rgba(0,0,0,.28);
    font-family: "Didact Gothic", "Century Gothic", sans-serif;
  }

  /* Contact side */
  .card--contact { background: var(--card-black); }
  .contact-body {
    position: absolute; left: 0; right: 0; top: 0; height: 252px;
    display: flex; flex-direction: column; align-items: center; justify-content: center;
    color: var(--ink-white); text-align: center;
  }
  .brand-mark {
    display: flex; align-items: center; gap: 8px; margin-bottom: 12px;
    font-size: 13px; letter-spacing: 2px; color: var(--ink-white);
  }
  .brand-mark__dot { width: 14px; height: 14px; border-radius: 50%; background: var(--ink-white); }
  .contact-name {
    font-family: "Montserrat", sans-serif; font-weight: 700; font-size: 19px; letter-spacing: .3px;
  }
  .contact-role { font-size: 12px; color: var(--ink-grey); margin: 2px 0 12px; }
  .contact-line { font-size: 14px; color: var(--ink-grey); line-height: 1.5; }
  .contact-line strong { color: var(--ink-white); font-weight: normal; letter-spacing: .5px; }
  .tagline-band {
    position: absolute; left: 0; right: 0; bottom: 0; height: 57px;
    background: var(--band-white);
    display: flex; align-items: center; padding-left: 22px;
    font-size: 17px; color: var(--ink-dark);
  }
  .tagline-band b { font-family: "Montserrat", sans-serif; font-weight: 800; margin-right: 5px; }

  /* Tagline side */
  .card--tagline {
    background: radial-gradient(circle at 75% 60%, var(--card-charcoal), var(--card-black) 70%);
  }
  .lens-photo {
    position: absolute; left: 0; top: 0; width: 320px; height: 260px;
    background: radial-gradient(ellipse at 30% 30%, var(--photo-teal) 0%, var(--photo-violet) 45%, rgba(21,21,21,0) 80%);
  }
  .tagline {
    position: absolute; right: 24px; top: 40px; text-align: right; color: var(--ink-white);
    font-family: "Montserrat", sans-serif; line-height: .95;
  }
  .tagline__capturing { display: block; font-weight: 700; font-size: 40px; }
  .tagline__lifes { display: block; font-weight: 400; font-size: 46px; }
  .tagline__moments { display: block; font-weight: 800; font-size: 62px; letter-spacing: -1px; }
  .studio-footer {
    position: absolute; left: 250px; bottom: 22px; color: var(--ink-grey);
  }
  .studio-name { font-size: 17px; color: var(--ink-white); letter-spacing: 1px; }
  .studio-web { font-size: 12px; margin-top: 4px; }
</style>
</head>
<body>
<main class="canvas">
  <section class="card card--contact" aria-label="Contact side">
    <div class="contact-body">
      <div class="brand-mark"><span class="brand-mark__dot"></span>Petra Voss Imaging</div>
      <div class="contact-name">Petra Voss-Hale</div>
      <div class="contact-role">Photographer</div>
      <div class="contact-line"><strong>555-318-0462</strong> - Cell and for SMS</div>
      <div class="contact-line">petra@petrastudioframes.com</div>
    </div>
    <div class="tagline-band"><b>Capturing</b> Life's Moments</div>
  </section>

  <section class="card card--tagline" aria-label="Tagline side">
    <div class="lens-photo" role="img" aria-label="Close-up photograph of a camera lens with teal and violet reflections"></div>
    <h1 class="tagline">
      <span class="tagline__capturing">Capturing</span>
      <span class="tagline__lifes">Life's</span>
      <span class="tagline__moments">Moments</span>
    </h1>
    <div class="studio-footer">
      <div class="studio-name">Petra Voss Imaging</div>
      <div class="studio-web">www.petravossimaging.com</div>
    </div>
  </section>
</main>
</body>
</html>
```